I need a great, modern, professional website for my paint contracting company, Ashbrook Coating Contractors, LLC. I have many good pix that can be used from jobs completed that would be attractive. We do commercial, residential and industrial jobs. I’m fully insured and licensed, including holding a General Contractor’s License as a Subcontractor. I know nothing about coding websites. I’ll have my assistant get on tomorrow and learn how to drop files. I’m not sure what files to send. This will be difficult at best, it being able to talk this through. Oh well. What’s next?

Target Market(s)

General Contractors

Industry/Entity Type

Paint Contracting

Coding

Coded - Design and coding required

Font styles to use
Sans Serif

Colors
00AB8E
00BBA5
67D7C9
C6EFE9
E9F9F6

Requirements
Must have
• Pix of completed jobs, bio, maybe testimonials from happy customers? ….
Nice to have
• I’d like it to have a modern appeal, but still have some warmth.
Should not have
• ??

```html
<!DOCTYPE html>
<html lang="en">
<head>
<meta charset="utf-8">
<title>Ashbrook Coating Contractors, LLC</title>
<link rel="stylesheet" href="https://fonts.googleapis.com/css2?family=Raleway:wght@400;500;600;700;800&family=Open+Sans:wght@400;600&family=Great+Vibes&display=swap">
<style>
:root{
  --ink:#1d2b2a;
  --text:#4f5c5a;
  --muted:#7d8a88;
  --teal-900:#00AB8E;
  --teal-700:#00BBA5;
  --teal-500:#67D7C9;
  --teal-200:#C6EFE9;
  --teal-100:#E9F9F6;
  --deep:#0d3b36;
  --footer:#0a2724;
  --white:#fff;
  --line:#d6ece8;
}
*{box-sizing:border-box;margin:0;padding:0}
html,body{width:1200px;height:4856px;overflow:hidden}
body{position:relative;background:var(--white);font-family:'Open Sans',sans-serif;color:var(--text);font-size:13px;line-height:1.6}
.abs{position:absolute}
h1,h2,h3,h4{font-family:'Raleway',sans-serif;color:var(--ink)}
.btn{display:inline-flex;align-items:center;gap:10px;background:var(--teal-900);color:#fff;font-family:'Raleway',sans-serif;font-size:11px;font-weight:700;letter-spacing:1px;padding:10px 18px;text-transform:uppercase}
.btn svg{width:14px;height:8px}
.more{color:var(--teal-900);font-size:10px;font-weight:700;letter-spacing:.5px;font-family:'Raleway',sans-serif;text-transform:uppercase}
.section-title{position:absolute;left:0;width:1200px;text-align:center;font-size:44px;font-weight:700}

/* header + hero */
.top-stripe{left:0;top:0;width:1200px;height:5px;background:linear-gradient(90deg,var(--teal-900),var(--teal-700),var(--teal-500),var(--teal-200))}
.hero{left:0;top:0;width:1200px;height:700px;background:linear-gradient(100deg,#5f6b69 0%,#9aa6a3 22%,#d3dcda 45%,#eef4f3 62%,#f6faf9 100%)}
.brand{left:120px;top:22px;color:#fff;font-family:'Raleway',sans-serif}
.brand-name{font-size:28px;font-weight:700;line-height:1}
.brand-sub{font-size:10px;font-weight:700;letter-spacing:3px;margin-top:4px}
.nav{left:530px;top:16px;display:flex;gap:4px}
.nav a{color:#fff;font-family:'Raleway',sans-serif;font-size:11px;font-weight:700;letter-spacing:1px;padding:10px 16px;text-decoration:none;background:rgba(0,0,0,.18)}
.nav a.active{background:var(--teal-900)}
.hero-copy{left:714px;top:170px;width:420px}
.hero-lead{font-family:'Raleway',sans-serif;font-size:30px;color:var(--ink);font-weight:500}
.hero-title{font-size:56px;font-weight:800;line-height:1.1;margin-top:4px}
.hero-script{font-family:'Great Vibes',cursive;font-size:84px;color:var(--teal-900);line-height:1;margin-top:-6px}
.hero-text{margin-top:16px;width:360px;font-size:14px}
.hero-copy .btn{margin-top:24px}

/* services */
.service{width:300px;text-align:center}
.diamond{width:212px;height:212px;margin:44px auto 0;transform:rotate(45deg)}
.service h3{margin-top:84px;font-size:19px;font-weight:600;letter-spacing:1.5px}
.service p{font-size:12px;width:250px;margin:6px auto 0;line-height:1.5}

/* welcome */
.welcome{left:108px;top:1345px;width:470px}
.eyebrow{font-family:'Raleway',sans-serif;font-size:15px;letter-spacing:2px;color:var(--teal-900);font-weight:600}
.welcome h2{font-size:38px;font-weight:700;line-height:1.15;margin-top:6px}
.welcome p{margin-top:22px;font-size:14px;line-height:1.7}
.welcome .btn{margin-top:30px}
.welcome-back{left:570px;top:1300px;width:140px;height:120px;background:var(--teal-200)}
.welcome-photo{left:636px;top:1255px;width:454px;height:545px;background:linear-gradient(160deg,#2e8b4a 0%,#7fbf8c 25%,#e7ece9 50%,#b8c0c8 75%,#5a6878 100%);border-top-left-radius:120px}

/* why choose */
.why-sub{left:0;top:1918px;width:1200px;text-align:center;font-size:14px}
.why-grid{left:108px;top:1975px;width:984px;display:grid;grid-template-columns:repeat(3,1fr)}
.why-item{height:260px;text-align:center;padding-top:22px}
.why-item:nth-child(-n+3){border-bottom:1px solid var(--line)}
.why-item:nth-child(3n+1),.why-item:nth-child(3n+2){border-right:1px solid var(--line)}
.why-icon{width:84px;height:84px;margin:0 auto;border-radius:14px}
.why-item h3{margin-top:22px;font-size:21px;font-weight:500;letter-spacing:1px}
.why-item p{font-size:13px;width:230px;margin:6px auto 10px;line-height:1.5}

/* projects */
.projects-band{left:0;top:2548px;width:1200px;height:652px;background:var(--teal-100)}
.project-main{left:108px;top:2670px;width:640px;height:440px;background:linear-gradient(90deg,#243a63 0%,#3b5b8c 18%,#f2c418 38%,#2e3a55 55%,#cfd2d6 80%,#8d9199 100%)}
.project-card{left:612px;top:2718px;width:480px;height:228px;background:#fff;padding:30px 36px;border-left:4px solid var(--teal-700)}
.project-card h3{font-size:24px;font-weight:600}
.project-card p{margin-top:12px;font-size:13px;line-height:1.6}
.project-card .btn{margin-top:18px}
.thumbs{left:380px;top:2960px;display:flex;gap:2px}
.thumbs div{width:177px;height:150px}

/* testimonials */
.quote{border-radius:70px;padding:24px 52px;font-size:13px;line-height:1.55}
.quote-a{left:140px;top:3410px;width:440px;height:150px;border:2px solid transparent;background:linear-gradient(#fff,#fff) padding-box,linear-gradient(90deg,var(--teal-900),var(--teal-500),var(--teal-200)) border-box}
.quote-b{left:620px;top:3452px;width:470px;height:150px;border:2px solid transparent;background:linear-gradient(#fff,#fff) padding-box,linear-gradient(90deg,var(--teal-200),var(--teal-700),var(--teal-900)) border-box}
.quote-mark{position:absolute;right:40px;bottom:8px;font-family:Georgia,serif;font-size:32px;color:var(--teal-500);line-height:1}
.author{display:flex;align-items:center;gap:12px}
.avatar{width:50px;height:50px;border-radius:50%;background:linear-gradient(135deg,#c9b7a8,#6e5a4e)}
.author strong{display:block;font-family:'Raleway',sans-serif;font-size:15px;color:var(--ink);font-weight:600;line-height:1.2}
.author span{font-size:11px;color:var(--muted)}
.dots{left:580px;top:3670px;display:flex;gap:6px}
.dots i{display:block;width:10px;height:4px;background:var(--teal-200)}
.dots i.on{background:var(--teal-900);width:18px}

/* blog */
.blog-band{left:0;top:3752px;width:1200px;height:568px;background:var(--teal-100)}
.blog-shade{left:0;top:4100px;width:0;height:0;border-left:190px solid var(--deep);border-top:220px solid transparent}
.blog-photo{left:40px;top:3880px;width:480px;height:440px;background:linear-gradient(135deg,#2f7de0 0%,#4da0f0 40%,#e9e2d6 65%,#c7bfb3 100%);clip-path:polygon(55% 0,100% 45%,100% 100%,0 100%,0 60%)}
.blog-title{left:572px;top:3790px;font-size:44px;font-weight:700}
.post{left:580px;width:512px;display:flex;gap:20px}
.post-thumb{width:190px;height:140px;flex:none}
.post h4{font-size:17px;font-weight:600;line-height:1.3;margin-top:4px}
.post p{font-size:12px;margin:8px 0 10px;line-height:1.5}

/* footer */
.footer{left:0;top:4320px;width:1200px;height:536px;background:var(--footer);color:var(--teal-200)}
.footer h4{color:#fff;font-size:22px;font-weight:600;margin-bottom:22px}
.footer .brand{position:absolute;left:120px;top:70px}
.f-about{left:120px;top:150px;width:250px;font-size:13px;line-height:1.6}
.socials{left:120px;top:260px;display:flex;gap:8px}
.socials i{display:block;width:28px;height:28px;border-radius:50%;background:var(--teal-900)}
.f-links{left:432px;top:70px}
.f-links a{display:block;color:var(--teal-200);text-decoration:none;font-size:13px;margin-bottom:14px}
.f-contact{left:628px;top:70px;width:230px}
.f-contact div{display:flex;gap:12px;align-items:flex-start;font-size:13px;margin-bottom:22px}
.f-contact .ic{width:26px;height:26px;border-radius:50%;border:1px solid var(--teal-700);display:flex;align-items:center;justify-content:center;flex:none}
.f-contact svg{width:12px;height:12px;fill:var(--teal-500)}
.f-news{left:876px;top:70px;width:220px}
.f-news .field{height:38px;border-radius:20px;background:#fff;color:#999;font-size:12px;padding:10px 16px}
.f-news .sub{margin-top:12px;height:38px;border-radius:20px;background:var(--teal-900);color:#fff;font-family:'Raleway',sans-serif;font-weight:700;font-size:12px;letter-spacing:1px;text-align:center;line-height:38px}
.copyright{left:0;top:4760px;width:1200px;border-top:1px solid #1c4540;padding-top:26px;text-align:center;font-size:13px;color:var(--teal-200)}
.copyright b{color:var(--teal-500);font-weight:400}
</style>
</head>
<body>

<!-- header + hero -->
<div class="abs hero" role="img" aria-label="Painter in work clothes and hard hat rolling white paint onto a wall"></div>
<div class="abs top-stripe"></div>
<div class="abs brand"><div class="brand-name">Ashbrook</div><div class="brand-sub">COATING CONTRACTORS</div></div>
<nav class="abs nav"><a class="active">HOME</a><a>ABOUT</a><a>SERVICE</a><a>PROJECTS</a><a>BLOG</a><a>CONTACT US</a></nav>
<div class="abs hero-copy">
  <div class="hero-lead">We Bring Your</div>
  <h1 class="hero-title">Home To Your</h1>
  <div class="hero-script">Dream</div>
  <p class="hero-text">Sed ut perspiciatis unde omnis iste natus error sit voluptatem accusantium.</p>
  <span class="btn">Read More <svg viewBox="0 0 14 8"><path d="M0 4h12M9 1l3 3-3 3" stroke="#fff" fill="none" stroke-width="1.3"/></svg></span>
</div>

<!-- services -->
<div class="abs service" style="left:70px;top:760px">
  <div class="diamond" role="img" aria-label="Crew painting a commercial building exterior" style="background:linear-gradient(135deg,#4aa65a,#a7c9a0 50%,#6b6257)"></div>
  <h3>COMMERCIAL PROJECTS</h3>
  <p>Sed ut perspiciatis unde omnis iste natus error sit voluptatem.</p>
</div>
<div class="abs service" style="left:450px;top:760px">
  <div class="diamond" role="img" aria-label="Homeowner rolling blue paint on a living room wall" style="background:linear-gradient(135deg,#1f7fe0,#4aa3f5 55%,#e8e1d8)"></div>
  <h3>REIDENTIAL PROJECTS</h3>
  <p>Sed ut perspiciatis unde omnis iste natus error sit voluptatem.</p>
</div>
<div class="abs service" style="left:830px;top:760px">
  <div class="diamond" role="img" aria-label="Contractor holding a fan of paint colour swatches" style="background:linear-gradient(135deg,#444,#d9534f 35%,#f5c242 55%,#5cb85c 75%,#3f7fd6)"></div>
  <h3>RESTORATION PROJECTS</h3>
  <p>Sed ut perspiciatis unde omnis iste natus error sit voluptatem.</p>
</div>

<!-- welcome -->
<div class="abs welcome">
  <div class="eyebrow">WELCOME TO</div>
  <h2>Ashbrook Coating<br>Contractors</h2>
  <p>Sed ut perspiciatis unde omnis iste natus error sit voluptatem accusantium doloremque laudantium, totam rem aperiam, eaque ipsa quae ab illo inventore veritatis et quasi architecto beatae vitae dicta sunt explicabo. Nemo enim ipsam voluptatem quia voluptas sit aspernatur aut odit aut fugit, sed quia consequuntur magni dolores eos qui ratione.</p>
  <span class="btn">Read More <svg viewBox="0 0 14 8"><path d="M0 4h12M9 1l3 3-3 3" stroke="#fff" fill="none" stroke-width="1.3"/></svg></span>
</div>
<div class="abs welcome-back"></div>
<div class="abs welcome-photo" role="img" aria-label="Painter in a hard hat rolling green paint across a white wall"></div>

<!-- why choose us -->
<h2 class="section-title" style="top:1848px">Why Choose Us?</h2>
<p class="abs why-sub">Sed ut perspiciatis unde omnis iste natus error sit voluptatem</p>
<div class="abs why-grid">
  <div class="why-item"><div class="why-icon" role="img" aria-label="Painter with roller illustration" style="background:linear-gradient(135deg,#f7c948,#7cc36b)"></div><h3>FAUX FINISHES</h3><p>Excepteur sint occaecat cupidatat non proident.</p><span class="more">View Details</span></div>
  <div class="why-item"><div class="why-icon" role="img" aria-label="Waterproofing drops illustration" style="background:linear-gradient(135deg,#5bb8f0,#1f6fbf)"></div><h3>WATER PROOFING</h3><p>Excepteur sint occaecat cupidatat non proident.</p><span class="more">View Details</span></div>
  <div class="why-item"><div class="why-icon" role="img" aria-label="Paint roller illustration" style="background:linear-gradient(135deg,#e3202c,#f5a623)"></div><h3>PRE-PAINT DEMO</h3><p>Excepteur sint occaecat cupidatat non proident.</p><span class="more">View Details</span></div>
  <div class="why-item"><div class="why-icon" role="img" aria-label="Scraper tool illustration" style="background:linear-gradient(135deg,#f2a33a,#5a4030)"></div><h3>MILDEW REMOVAL</h3><p>Excepteur sint occaecat cupidatat non proident.</p><span class="more">View Details</span></div>
  <div class="why-item"><div class="why-icon" role="img" aria-label="Colour swatch fan illustration" style="background:linear-gradient(135deg,#e3202c,#f7c948 35%,#5cb85c 65%,#3f7fd6)"></div><h3>COLOR PROOF</h3><p>Excepteur sint occaecat cupidatat non proident.</p><span class="more">View Details</span></div>
  <div class="why-item"><div class="why-icon" role="img" aria-label="Paint bucket illustration" style="background:linear-gradient(135deg,#4aa3f5,#c0392b)"></div><h3>WINDOW WASHING</h3><p>Excepteur sint occaecat cupidatat non proident.</p><span class="more">View Details</span></div>
</div>

<!-- recent projects -->
<div class="abs projects-band"></div>
<h2 class="section-title" style="top:2586px">Recent Projects</h2>
<div class="abs project-main" role="img" aria-label="Bedroom with navy and yellow striped feature wall"></div>
<div class="abs project-card">
  <h3>Bedroom Wall Design</h3>
  <p>Sed ut perspiciatis unde omnis iste natus error sit voluptatem accusantium doloremque laudantium, totam rem aperiam, eaque ipsa quae ab illo inventore veritatis et quasi architecto.</p>
  <span class="btn">More Projects <svg viewBox="0 0 14 8"><path d="M0 4h12M9 1l3 3-3 3" stroke="#fff" fill="none" stroke-width="1.3"/></svg></span>
</div>
<div class="abs thumbs">
  <div role="img" aria-label="Dark grey living room" style="background:linear-gradient(135deg,#3d3d3d,#7a7a7a)"></div>
  <div role="img" aria-label="Navy painted room interior" style="background:linear-gradient(135deg,#1f2a44,#4a5a7a)"></div>
  <div role="img" aria-label="Purple accent wall" style="background:linear-gradient(135deg,#5d2a7a,#c9c2d6)"></div>
  <div role="img" aria-label="Red painted dining room" style="background:linear-gradient(135deg,#a52a2a,#d9b38c)"></div>
</div>

<!-- testimonials -->
<h2 class="section-title" style="top:3316px">Testimonials</h2>
<div class="abs quote quote-a">Sed ut perspiciatis unde omnis iste natus error sit voluptatem accusantium doloremque laudantium, totam rem aperiam, eaque ipsa quae ab illo inventore veritatis et quasi architecto beatae vitae dicta sunt explicabo.<span class="quote-mark">&rdquo;</span></div>
<div class="abs author" style="left:186px;top:3572px"><div class="avatar" role="img" aria-label="Customer portrait"></div><div><strong>Marcus Delaney</strong><span>Manager, Westvale</span></div></div>
<div class="abs quote quote-b">Sed ut perspiciatis unde omnis iste natus error sit voluptatem accusantium doloremque laudantium, totam rem aperiam, eaque ipsa quae ab illo inventore veritatis et quasi architecto beatae vitae dicta sunt explicabo.<span class="quote-mark">&rdquo;</span></div>
<div class="abs author" style="left:716px;top:3614px"><div class="avatar" role="img" aria-label="Customer portrait"></div><div><strong>Clara Whitfield</strong><span>Manager, Westvale</span></div></div>
<div class="abs dots"><i class="on"></i><i></i><i></i></div>

<!-- blog -->
<div class="abs blog-band"></div>
<div class="abs blog-shade"></div>
<div class="abs blog-photo" role="img" aria-label="Smiling couple holding paint rollers in front of a blue wall"></div>
<h2 class="abs blog-title">Recent Blog</h2>
<div class="abs post" style="top:3880px"><div class="post-thumb" role="img" aria-label="Painters working on a ceiling" style="background:linear-gradient(135deg,#3a7bd5,#a8c6e8)"></div><div><h4>Excepteur sint occaecat cupidatat non proident</h4><p>Sed ut perspiciatis unde omnis iste natus et voluptatem...</p><span class="more">Read More</span></div></div>
<div class="abs post" style="top:4030px"><div class="post-thumb" role="img" aria-label="Red brick building being painted" style="background:linear-gradient(135deg,#c0392b,#e8b4a8)"></div><div><h4>Excepteur sint occaecat cupidatat non proident</h4><p>Sed ut perspiciatis unde omnis iste natus et voluptatem...</p><span class="more">Read More</span></div></div>
<div class="abs post" style="top:4180px"><div class="post-thumb" role="img" aria-label="Painter rolling a grey wall" style="background:linear-gradient(135deg,#6b5a4a,#d8cfc4)"></div><div><h4>Excepteur sint occaecat cupidatat non proident</h4><p>Sed ut perspiciatis unde omnis iste natus et voluptatem...</p><span class="more">Read More</span></div></div>

<!-- footer -->
<footer class="abs footer">
  <div class="brand"><div class="brand-name">Ashbrook</div><div class="brand-sub">COATING CONTRACTORS</div></div>
  <p class="abs f-about">Sed ut perspiciatis unde omnis iste natus error sit voluptatem accusantium doloremque laudantium, totam rem aperiam.</p>
  <div class="abs socials"><i></i><i></i><i></i></div>
  <div class="abs f-links"><h4>Quick Links</h4><a>About Us</a><a>Services</a><a>Projects</a><a>Blog</a><a>Contact Us</a></div>
  <div class="abs f-contact"><h4>Contact Us</h4>
    <div><span class="ic"><svg viewBox="0 0 12 12"><path d="M6 0a4 4 0 0 0-4 4c0 3 4 8 4 8s4-5 4-8a4 4 0 0 0-4-4zm0 5.5A1.5 1.5 0 1 1 6 2.5a1.5 1.5 0 0 1 0 3z"/></svg></span><span>2050 Birchwood Lane,<br>Ashbrook, CA 10234</span></div>
    <div><span class="ic"><svg viewBox="0 0 12 12"><path d="M2.5 0 4.5 2.5 3.3 4a7 7 0 0 0 4.7 4.7L9.5 7.5 12 9.5 10.5 12C5 12 0 7 0 1.5z"/></svg></span><span>(+1) 555 014 2290</span></div>
    <div><span class="ic"><svg viewBox="0 0 12 12"><path d="M0 2h12v8H0zm1 1 5 4 5-4"/></svg></span><span>info@ashbrookcoating.com</span></div>
  </div>
  <div class="abs f-news"><h4>Newsletter</h4><div class="field">Enter Email</div><div class="sub">SUBSCRIBE</div></div>
</footer>
<div class="abs copyright">Copyright © 2023 <b>Ashbrook Coating Contractors, LLC</b>. All rights reserved.</div>

</body>
</html>
```